Corporate Design für Sachverständigerbüro
Zielgruppe
freiberufliche Tätigkeit als öffentlich bestellter und vereidigter Sachverständiger
Erstellung von landwirtschaftlichen und insolvenzspezifischen Gutachten, betriebswirtschaftliche Beratung, Betriebsfortführung, Unternehmensbewertung
Zielgruppe: Insovenzverwalter, Rechtsanwälte, Steuerberater, Landwirte
Aufgabenstellung
Nennung des Names, der öffentlichen Bestellung sowie Sachverständigenbüro Harald Kessing;
Gerne dunkelgrüne Logoelemente; Logo eher schlicht; Deisign sollte Seriösität, Vertrauen und Fachkompetenz kommunizieren

```html
<!DOCTYPE html>
<html lang="de">
<head>
<meta charset="utf-8">
<title>Sachverständigenbüro Harald Kessing – Visitenkarte</title>
<link rel="stylesheet" href="https://fonts.googleapis.com/css2?family=Open+Sans:wght@300;400;600&display=swap">
<style>
  :root {
    --frame-green: #9caf7e;
    --dark-green: #17563a;
    --sage: #98a877;
    --band-light: #e9e9bd;
    --band-dark: #9db07f;
    --band-text: #2e6643;
    --card-white: #ffffff;
    --card-tint: #f3f3f3;
    --page: #ffffff;
    --stage: #f1f1ef;
  }
  * { margin: 0; padding: 0; box-sizing: border-box; }
  html, body { width: 1200px; height: 2401px; overflow: hidden; background: var(--page); }
  body { font-family: "Open Sans", Arial, sans-serif; position: relative; }

  .presentation-frame {
    position: absolute; left: 0; top: 0; width: 1200px; height: 1168px;
    border: 5px solid var(--frame-green); background: var(--page);
  }
  .stage-area {
    position: absolute; left: 0; top: 1176px; width: 1200px; height: 1225px;
    background: var(--stage);
  }

  .business-card {
    position: absolute; width: 627px; height: 405px;
    background: linear-gradient(115deg, var(--card-white) 0%, var(--card-tint) 55%, var(--card-white) 100%);
    box-shadow: 1px 1px 2px rgba(0,0,0,0.25);
    overflow: hidden;
  }
  .card--flat { left: 326px; top: 452px; }
  .card--large { left: 286px; top: 1586px; transform: scale(1.4); transform-origin: 0 0; left: 161px; }

  .brand-mark {
    position: absolute; left: 72px; top: 118px; width: 78px; height: 78px;
    border-radius: 50%; background: var(--dark-green);
  }
  .brand-divider {
    position: absolute; left: 171px; top: 118px; width: 1px; height: 80px; background: #8a8a8a;
  }
  .brand-name {
    position: absolute; left: 194px; top: 118px;
    font-size: 31px; font-weight: 600; color: var(--dark-green); letter-spacing: 0.2px; line-height: 1.1;
  }
  .brand-title {
    position: absolute; left: 194px; top: 158px;
    font-size: 24px; font-weight: 600; color: var(--sage); line-height: 1.1;
  }
  .appointment-band {
    position: absolute; left: 0; bottom: 0; width: 100%; height: 118px;
    border-top: 1px solid var(--dark-green);
    background: linear-gradient(180deg, var(--band-light) 0%, var(--band-dark) 100%);
    display: flex; align-items: center; justify-content: center;
  }
  .appointment-text {
    font-size: 19px; font-weight: 300; color: var(--band-text); margin-top: -4px;
  }
</style>
</head>
<body>
  <section class="presentation-frame">
    <article class="business-card card--flat">
      <div class="brand-mark" aria-hidden="true"></div>
      <div class="brand-divider"></div>
      <p class="brand-name">Sachverständigenbüro</p>
      <p class="brand-title">Dipl.-Ing. agrar Harald Kessing</p>
      <div class="appointment-band">
        <p class="appointment-text">öffentlich bestellter und vereidigter Sachverständiger</p>
      </div>
    </article>
  </section>

  <section class="stage-area">
    <article class="business-card card--large" style="top:410px;">
      <div class="brand-mark" aria-hidden="true"></div>
      <div class="brand-divider"></div>
      <p class="brand-name">Sachverständigenbüro</p>
      <p class="brand-title">Dipl.-Ing. agrar Harald Kessing</p>
      <div class="appointment-band">
        <p class="appointment-text">öffentlich bestellter und vereidigter Sachverständiger</p>
      </div>
    </article>
  </section>
</body>
</html>
```